Business Card Design

Cedar Gate Rentals
Cedar Gate Rentals is a high end home rental leasing company that provides exquisite properties in niche markets. We are a small family owned business that considers our clients not as renters, but as friends. Every property we buy must be brought up to our high standards before it is offered on the market. The properties that we lease are exceptional, "move in" ready homes. This allows for the client to take pride in their lease as if it was their own home. To put it another way; we do not lease a property that we would not live in ourselves.

Target Market(s)

Couples making $100K or more

Industry/Entity Type

Business

Requirements
Must have
• Some sort of logo
Nice to have
• good slogan
Should not have
• Pink

```html
<!DOCTYPE html>
<html lang="en">
<head>
<meta charset="utf-8">
<title>Cedar Gate Rentals – Business Card</title>
<link rel="stylesheet" href="https://fonts.googleapis.com/css2?family=Arimo:wght@400;700&display=swap">
<style>
  :root {
    --sky: #6acef5;
    --lime: #c9de5e;
    --paper: #ffffff;
    --ink-light: #ffffff;
  }
  * { margin: 0; padding: 0; box-sizing: border-box; }
  html, body {
    width: 1200px;
    height: 704px;
    overflow: hidden;
    background: var(--paper);
    font-family: "Arimo", Arial, sans-serif;
  }
  .card {
    position: relative;
    width: 1200px;
    height: 704px;
    background: var(--paper);
  }
  .brand-mark {
    position: absolute;
    left: 130px;
    top: 71px;
    width: 165px;
    height: 165px;
    background: var(--sky);
  }
  .brand-name {
    position: absolute;
    left: 317px;
    top: 104px;
    font-size: 48px;
    font-weight: 700;
    line-height: 1;
    color: var(--lime);
    white-space: nowrap;
  }
  .slogan {
    position: absolute;
    left: 317px;
    top: 170px;
    font-size: 29px;
    font-weight: 400;
    line-height: 1;
    color: var(--sky);
    white-space: nowrap;
  }
  .contact-band {
    position: absolute;
    left: 0;
    top: 287px;
    width: 1200px;
    height: 286px;
    background: var(--sky);
    color: var(--ink-light);
  }
  .person-name {
    position: absolute;
    left: 130px;
    top: 95px;
    font-size: 36px;
    font-weight: 700;
    line-height: 1;
  }
  .person-role {
    position: absolute;
    left: 130px;
    top: 151px;
    font-size: 32px;
    font-weight: 400;
    line-height: 1;
  }
  .phone {
    position: absolute;
    left: 502px;
    top: 96px;
    font-size: 34px;
    font-weight: 400;
    line-height: 1;
  }
  .email {
    position: absolute;
    left: 502px;
    top: 151px;
    font-size: 34px;
    font-weight: 400;
    line-height: 1;
  }
  .address-band {
    position: absolute;
    left: 0;
    top: 573px;
    width: 1200px;
    height: 131px;
    background: var(--lime);
  }
  .address {
    position: absolute;
    left: 130px;
    top: 50px;
    font-size: 28px;
    font-weight: 400;
    line-height: 1;
    letter-spacing: 1.4px;
    color: var(--ink-light);
    white-space: nowrap;
  }
</style>
</head>
<body>
  <main class="card">
    <div class="brand-mark" aria-hidden="true"></div>
    <h1 class="brand-name">CedarGateRentals</h1>
    <p class="slogan">Your next dream house</p>

    <section class="contact-band">
      <p class="person-name">MARLOWE</p>
      <p class="person-role">General Manager</p>
      <p class="phone">+1 202 5550143</p>
      <p class="email">hello@cedargaterentals.com</p>
    </section>

    <footer class="address-band">
      <p class="address">82 Linden Street, Apt. 210. New York, NY 10016. Code Post</p>
    </footer>
  </main>
</body>
</html>
```